Flyer-Design für Zweithaar Studio
Zielgruppe
Firma MOLVA Ketz ist ein Zweithaar Studio. Hier erhalten Kunden individuell auf sie zugeschnittene Perücken und Toupets. Unsere Zielgruppe sind Männer und Frauen mit wenig oder keiner Kopfbehaarung oder Menschen die krankheitsbedingt unter Haarausfall leiden.
Aufgabenstellung
Bitte Vorschläge zu Anzahl Seiten und Format erstellen, aktuell haben wir noch keine Vorstellung dazu. Folgende Inhalte haben wir schon mal als Entwurf vorbereitet:
Eine Seite zum Thema Toupets mit dem Bild vom Mann:
Leiden Sie an übermäßigem Haarausfall?
Fühlen Sie sich nicht mehr 100% wohl damit und möchten gerne wieder Ihre Attraktivität und vor allem das Wohlbefinden steigern?
Dann sind Sie bei uns sehr gut aufgehoben, denn wir können Ihnen Ihr Toupet individuell auf Ihre Bedürfnisse hin z.B. Farbe, Grauanteil, Größe und Styling anpassen.
Eine Seite zum Thema Perücken mit dem Bild der Frau:
Sind Sie an einer Perücke interessiert die augenscheinlich keinen Unterschied zu gewachsenem Haar aufweist?
Dann sind Sie bei uns an der richtigen Adresse. Die langjährige Erfahrung im Zweithaar Bereich von Friseurmeisterin verspricht Ihnen optimale Beratung und ein individuell auf Sie abgestimmtes Produkt.
Bei uns erhalten Sie Zugriff auf verschiedene Modelle im gesamten Preisspektrum.
Liegt eine von Ihrem Arzt attestierte Erkrankung vor, übernimmt Ihre Krankenkasse höchstwahrscheinlich die Kosten für Ihr Zweithaar. Die Formalitäten dazu erledigen wir gerne für Sie um Ihnen unnötigen Stress zu ersparen.
Eine weitere Seite mit den besonderen Merkmalen mit dem Bild Diversity:
Mit unserer Befestigungsmethode sind Sie sehr flexibel - starker halt für jede Situation und auf Wunsch auch abnehmbar z.B. nachts beim schlafen.
Der große Vorteil unserer Befestigungsmethode liegt darin, dass Sie diese selbst umsetzen können und somit nicht jeden Monat das Studio zur Neubefestigung aufsuchen müssen. Das spart Ihnen Zeit und Geld.
Wir können Ihnen Toupets und Perücken in allen Preisklassen anbieten, in verschiedenen Farben, auf Wunsch mit Grauanteil passend zum Alter des Trägers. Unsere Friseurmeisterin Frau Tiltrop berät Sie gerne, natürlich unverbindlich und kostenlos.

```html
<!DOCTYPE html>
<html lang="de">
<head>
<meta charset="utf-8">
<title>MOLVA Ketz – Flyer Zweithaar Studio</title>
<link href="https://fonts.googleapis.com/css2?family=Open+Sans:ital,wght@0,400;0,600;0,700;1,400&display=swap" rel="stylesheet">
<style>
:root{
  --stage:#e9e9ea;
  --grey:#6d6e70;
  --grey-dark:#58595b;
  --grey-light:#c9cacc;
  --tag:#d6d7d9;
  --paper:#f6f6f6;
  --white:#ffffff;
  --text:#5a5b5d;
}
*{box-sizing:border-box;margin:0;padding:0}
html,body{width:1200px;height:2960px;overflow:hidden;background:var(--stage);font-family:'Open Sans',sans-serif;color:var(--text)}
.spread{position:absolute;left:60px;width:1080px;height:760px;display:flex;box-shadow:0 20px 50px rgba(0,0,0,.18)}
.spread--outside{top:600px}
.spread--inside{top:1600px}
.panel{position:relative;width:360px;height:760px;overflow:hidden}
.panel--grey{background:var(--grey);color:var(--white)}
.panel--paper{background:var(--paper)}
.photo{position:absolute;left:0;width:100%}
.tag{display:inline-block;background:var(--tag);color:var(--grey-dark);text-transform:uppercase;font-size:12px;letter-spacing:1px;padding:3px 12px;margin-bottom:4px}
.tag--big{font-size:15px;padding:4px 14px}
.wordmark{font-weight:700;letter-spacing:3px;text-transform:uppercase;color:var(--grey)}
.body{font-size:11px;line-height:1.55}
.body p{margin-bottom:8px}

/* cover */
.cover .head{height:150px;background:var(--white);text-align:center;padding-top:38px}
.cover .wordmark{font-size:30px}
.cover .rule{width:160px;height:2px;background:var(--grey-light);margin:10px auto 0}
.cover .frame{position:absolute;top:150px;left:0;width:360px;height:360px}
.cover .photo{top:150px;left:40px;width:280px;height:320px;clip-path:polygon(0 0,100% 0,100% 72%,50% 100%,0 72%);background:linear-gradient(160deg,#8a6a55,#4a372c 70%,#2f2520)}
.cover .cta{position:absolute;top:380px;right:24px;text-align:right}
.cover .cta .tag{display:block;font-size:15px}
.cover .headline{position:absolute;top:560px;left:0;width:100%;text-align:center;font-weight:700;font-size:34px;line-height:1.1;text-transform:uppercase;letter-spacing:1px}
.cover .headline small{font-size:15px;font-weight:400}
.cover .url{position:absolute;bottom:36px;width:100%;text-align:center;font-size:12px}

/* back */
.back{padding-top:40px;text-align:center}
.back .tags .tag{display:table;margin:0 auto 4px}
.back .wordmark{color:var(--white);font-size:30px;margin-top:90px}
.back .wordmark-rule{width:150px;height:2px;background:rgba(255,255,255,.5);margin:10px auto 0}
.contact{margin:70px 40px 0;font-size:11px;line-height:1.6}
.contact .row{border-top:1px solid rgba(255,255,255,.55);padding:14px 0 16px;position:relative}
.contact .row svg{position:absolute;top:-9px;left:50%;margin-left:-9px;background:var(--grey);padding:0 2px}
.contact b{font-weight:700}

/* wig panel */
.wig .photo{top:0;height:250px;background:radial-gradient(circle at 50% 40%,#9b3a2c,#3a1c18 55%,#1c1414)}
.wig .intro{position:absolute;top:268px;left:26px;right:26px;font-weight:700;font-size:12px;line-height:1.4}
.wig .tags{position:absolute;top:318px;left:26px}
.wig .items{position:absolute;top:400px;left:26px;right:24px}
.item{display:flex;gap:14px;margin-bottom:14px;font-size:12px;line-height:1.5}
.item svg{flex:0 0 30px}

/* toupet panel */
.toupet .photo{top:0;height:210px;background:linear-gradient(120deg,#20262e,#3f4650 60%,#6b6660)}
.toupet .questions{position:absolute;top:236px;left:28px;right:20px;text-transform:uppercase;font-size:14px;line-height:1.35;letter-spacing:.5px;color:var(--grey)}
.toupet .questions p{margin-bottom:14px}
.toupet .tags{position:absolute;top:430px;left:28px}
.toupet .fit{position:absolute;top:500px;left:0;width:100%;height:260px;background:var(--grey);color:var(--white);padding:22px 28px}
.toupet .fit h3{font-size:12px;font-weight:700;font-style:italic;line-height:1.4;margin-bottom:18px}
.features{display:grid;grid-template-columns:1fr 1fr;gap:16px 10px}
.features span{display:flex;align-items:center;gap:10px;font-size:14px;text-transform:uppercase;letter-spacing:1px}

/* advice panel */
.advice{background:var(--paper)}
.advice .box{position:absolute;top:24px;left:22px;right:22px;height:470px;background:var(--grey);color:var(--white);padding:22px 22px}
.advice .tag{margin-bottom:14px}
.advice .body{font-size:10.5px}
.advice .lines{margin-top:14px;font-size:12px;font-weight:700;line-height:2}
.advice .lines span{display:flex;align-items:center;gap:10px}
.advice .photo{top:510px;height:250px;background:linear-gradient(100deg,#e9e3dc,#c7b29a 45%,#e7e2db)}

/* visit panel */
.visit{background:var(--white);padding:34px 26px 0}
.visit .logo{text-align:center}
.visit .wordmark{font-size:28px}
.visit .rule{width:150px;height:2px;background:var(--grey-light);margin:8px auto 18px}
.visit .body{font-size:10.5px;margin-top:10px}
.hours-title{display:flex;align-items:center;gap:10px;font-size:14px;letter-spacing:1px;text-transform:uppercase;color:var(--grey);margin:14px 0 10px}
.hours{font-size:11px;border-collapse:collapse;width:100%}
.hours td{padding:1px 0}
.hours td:last-child{padding-left:20px}
</style>
</head>
<body>

<section class="spread spread--outside">
  <article class="panel panel--paper wig">
    <div class="photo" role="img" aria-label="Foto: Frau mit langen roten Haaren vor dunklem Hintergrund"></div>
    <p class="intro">Sind Sie an einer Perücke interessiert die augenscheinlich keinen Unterschied zu gewachsenem Haar aufweist?</p>
    <div class="tags">
      <span class="tag tag--big">Dann sind Sie bei uns an der</span><br>
      <span class="tag tag--big">richtigen Adresse</span>
    </div>
    <div class="items">
      <div class="item">
        <svg width="30" height="30" viewBox="0 0 30 30"><circle cx="15" cy="13" r="9" fill="none" stroke="#6d6e70" stroke-width="2.5"/><circle cx="15" cy="13" r="4" fill="#6d6e70"/><path d="M9 20l-3 8 5-2 2 3 2-7M21 20l3 8-5-2-2 3-2-7" fill="#6d6e70"/></svg>
        <p>Die langjährige Erfahrung im Zweithaar Bereich von Friseurmeisterin Marlene Tiltrop verspricht Ihnen optimale Beratung und ein individuell auf Sie abgestimmtes Produkt.</p>
      </div>
      <div class="item">
        <svg width="30" height="30" viewBox="0 0 30 30" fill="#6d6e70"><rect x="2" y="18" width="6" height="8"/><rect x="9" y="14" width="6" height="12"/><rect x="16" y="10" width="6" height="16"/><rect x="23" y="6" width="6" height="20"/></svg>
        <p>Bei uns erhalten Sie Zugriff auf verschiedene Modelle im gesamten Preisspektrum.</p>
      </div>
      <div class="item">
        <svg width="30" height="30" viewBox="0 0 30 30"><rect x="5" y="3" width="20" height="24" rx="2" fill="none" stroke="#6d6e70" stroke-width="2.5"/><path d="M10 10h10M10 15h10M10 20h6" stroke="#6d6e70" stroke-width="2"/></svg>
        <p>Liegt eine von Ihrem Arzt attestierte Erkrankung vor, übernimmt Ihre Krankenkasse höchstwahrscheinlich die Kosten für Ihr Zweithaar. Die Formalitäten dazu erledigen wir gerne für Sie um Ihnen unnötigen Stress zu ersparen.</p>
      </div>
    </div>
  </article>

  <article class="panel panel--grey back">
    <div class="tags">
      <span class="tag">Kostenlos und unverbindlich</span>
      <span class="tag">beraten lassen!</span>
    </div>
    <div class="wordmark">MOLVA KETZ</div>
    <div class="wordmark-rule"></div>
    <div class="contact">
      <div class="row">
        <svg width="18" height="18" viewBox="0 0 18 18" fill="#fff"><circle cx="9" cy="6" r="3.5"/><path d="M2 17c0-4 3-6 7-6s7 2 7 6z"/></svg>
        <b>MOLVA Ketz | Marlene Tiltrop</b><br>Lindenhofer Straße 12<br>44135 Dortmund
      </div>
      <div class="row">
        <svg width="18" height="18" viewBox="0 0 18 18" fill="#fff"><path d="M4 2l3 0 1 4-2 1.5a9 9 0 0 0 4.5 4.5L12 10l4 1v3a2 2 0 0 1-2 2C8 16 2 10 2 4a2 2 0 0 1 2-2z"/></svg>
        <b>Festnetz:</b> 0231 48 70 29 16<br><b>Mobil:</b> 0176 55 21 84 30
      </div>
      <div class="row">
        <svg width="18" height="18" viewBox="0 0 18 18" fill="#fff"><rect x="2" y="4" width="14" height="10"/><path d="M2 4l7 6 7-6" stroke="#6d6e70" stroke-width="1.5" fill="none"/></svg>
        <b>Email:</b> info@molva-ketz.de
      </div>
      <div class="row">
        <svg width="18" height="18" viewBox="0 0 18 18" fill="none" stroke="#fff" stroke-width="1.5"><circle cx="9" cy="9" r="7"/><path d="M2 9h14M9 2c3 3 3 11 0 14M9 2c-3 3-3 11 0 14"/></svg>
        <b>www.molva-ketz.de</b>
      </div>
    </div>
  </article>

  <article class="panel panel--grey cover">
    <div class="head">
      <div class="wordmark">MOLVA KETZ</div>
      <div class="rule"></div>
    </div>
    <svg class="frame" viewBox="0 0 360 360"><polyline points="20,20 20,260 180,340 340,260 340,20" fill="none" stroke="#fff" stroke-width="8"/></svg>
    <div class="photo" role="img" aria-label="Foto: Frau mit langem, welligem braunem Haar"></div>
    <div class="cta">
      <span class="tag">Jetzt Termin</span>
      <span class="tag">vereinbaren</span>
    </div>
    <h1 class="headline">Perücken <small>und</small><br>Toupets!</h1>
    <div class="url">www.molva-ketz.de</div>
  </article>
</section>

<section class="spread spread--inside">
  <article class="panel panel--paper toupet">
    <div class="photo" role="img" aria-label="Foto: Mann mit gepflegter Frisur in dunklem Raum"></div>
    <div class="questions">
      <p>Leiden Sie an übermäßigem Haarausfall?</p>
      <p>Fühlen Sie sich nicht mehr 100% wohl damit?</p>
      <p>Möchten Sie Ihre Attraktivität und Ihr Wohlbefinden steigern?</p>
    </div>
    <div class="tags">
      <span class="tag tag--big">Dann sind Sie bei uns</span><br>
      <span class="tag tag--big">genau richtig!</span>
    </div>
    <div class="fit">
      <h3>Wir passen Ihr Toupet individuell und auf Ihre Bedürfnisse an:</h3>
      <div class="features">
        <span><svg width="24" height="20" viewBox="0 0 24 20" fill="#fff"><rect x="0" y="12" width="5" height="8"/><rect x="6" y="8" width="5" height="12"/><rect x="12" y="4" width="5" height="16"/><rect x="18" y="0" width="5" height="20"/></svg>Farbe</span>
        <span><svg width="24" height="20" viewBox="0 0 24 20" fill="none" stroke="#fff" stroke-width="2"><path d="M2 14h20v5H2z"/><path d="M4 10c2-6 14-6 16 0"/></svg>Grauanteil</span>
        <span><svg width="24" height="20" viewBox="0 0 24 20" fill="none" stroke="#fff" stroke-width="2"><rect x="1" y="7" width="22" height="7"/><path d="M5 7v3M9 7v4M13 7v3M17 7v4"/></svg>Größe</span>
        <span><svg width="24" height="20" viewBox="0 0 24 20" fill="none" stroke="#fff" stroke-width="2"><circle cx="5" cy="15" r="3"/><circle cx="5" cy="5" r="3"/><path d="M7 6l15 10M7 14L22 4"/></svg>Styling</span>
      </div>
    </div>
  </article>

  <article class="panel advice">
    <div class="box">
      <span class="tag">Wir beraten Sie gerne!</span>
      <div class="body">
        <p>Mit unserer Befestigungsmethode sind Sie sehr flexibel - starker Halt für jede Situation und auf Wunsch auch abnehmbar zum Beispiel nachts beim Schlafen.</p>
        <p>Der große Vorteil unserer Befestigungsmethode liegt darin, dass Sie diese selbst umsetzen können und somit nicht jeden Monat das Studio zur Neubefestigung aufsuchen müssen. <b>Das spart Ihnen Zeit und Geld.</b></p>
        <p>Wir können Ihnen Toupets und Perücken in allen Preisklassen anbieten, in verschiedenen Farben, auf Wunsch mit Grauanteil passend zum Alter des Trägers.</p>
        <p>Unsere Friseurmeisterin Frau Tiltrop berät Sie gerne, natürlich unverbindlich und kostenlos.</p>
      </div>
      <div class="lines">
        <span><svg width="14" height="14" viewBox="0 0 18 18" fill="#fff"><path d="M4 2l3 0 1 4-2 1.5a9 9 0 0 0 4.5 4.5L12 10l4 1v3a2 2 0 0 1-2 2C8 16 2 10 2 4a2 2 0 0 1 2-2z"/></svg>0231 - 48 70 29 16</span>
        <span><svg width="14" height="14" viewBox="0 0 18 18" fill="#fff"><rect x="2" y="4" width="14" height="10"/><path d="M2 4l7 6 7-6" stroke="#6d6e70" stroke-width="1.5" fill="none"/></svg>info@molva-ketz.de</span>
      </div>
    </div>
    <div class="photo" role="img" aria-label="Foto: Friseurin schneidet einer blonden Kundin die Haare im hellen Salon"></div>
  </article>

  <article class="panel visit">
    <div class="logo">
      <div class="wordmark">MOLVA KETZ</div>
      <div class="rule"></div>
    </div>
    <span class="tag">Besuchen Sie uns!</span>
    <div class="body">
      <p>Unser Zweithaar Studio befindet sich im ersten Obergeschoss eines barrierefrei zugänglichen Ärztehauses. Es arbeiten mehrere Praxen in dem Gebäude, daher können Sie völlig unauffällig unser Studio erreichen.</p>
      <p>Frau Tiltrop freut sich Sie in unserem Studio begrüßen zu dürfen.</p>
      <p>Während Ihres Termins sind Sie der einzige Kunde vor Ort, es werden keine Paralleltermine vereinbart. Ein Sichtschutz trennt den Arbeitsbereich vom Eingangsbereich im Studio für den Fall dass spontan ein Kunde z.B. Zubehör abholen möchte.</p>
      <p>Wenn Sie von uns Zubehör postalisch erhalten möchten wird das Paket in einer neutralen Verpackung geliefert. Da sich unser Studio im Ärztehaus direkt neben dem Frischmarkt Heller in Aplerbeck befindet haben Sie dort genügend Parkplätze auf 2 Etagen zur Auswahl. Diese sind auch barrierefrei zugänglich.</p>
      <p>Für alle Kunden die mit den öffentlichen Verkehrsmitteln anreisen haben wir auch gute Nachrichten. Die nächste Bahn und U-Bahn Station befinden sich nur 2-3 Gehminuten von uns entfernt.</p>
    </div>
    <div class="hours-title">
      <svg width="22" height="22" viewBox="0 0 22 22"><circle cx="11" cy="11" r="10" fill="#6d6e70"/><path d="M11 5v6h5" stroke="#fff" stroke-width="2" fill="none"/></svg>
      Öffnungszeiten
    </div>
    <table class="hours">
      <tr><td>Montag:</td><td>geschlossen</td></tr>
      <tr><td>Dienstag - Freitag:</td><td>09:30h - 18:00h</td></tr>
      <tr><td>Samstag:</td><td>nach Terminvereinbarung</td></tr>
    </table>
  </article>
</section>

</body>
</html>
```